Makeup artist looking for business card design

- Business card to be memorable and recognisable

- I've attached photos of my logo (File 4), photos that I want to incorporate into the design (File 5,6 & 7) and an example of the design I like "Mirela Stott" (File 1)

- I've attached 3 photos of the designs I want to use, please use one of your choice

- Next to Instagram (File 2) and Facebook (File 3), please use their logo.

- No coloured background, either use the original background (grey) old white.

- Please include the following on the business card:
- Business name: LK Makeup Artistry
- My name: Rosalind Kerr
- Occupation: Makeup Artist
- Contact number: 0437 295 148
- Email: roskerr_makeup@mailvento.com
- Instagram (please use image): @lkmakeupartistry
- Facebook (please use image): www.mybeautypage.net/LKMakeUpArtistry

Target Market(s)

Target woman for bridal makeup, occasion, fashion makeup and print.

Industry/Entity Type

Business

Requirements
Must have
• Logo provided and photo provided
Should not have
• Colourful background
Too cluttered
Shouldn't use old style font

```html
<!DOCTYPE html>
<html lang="en">
<head>
<meta charset="utf-8">
<title>Rosalind Kerr – Business Card</title>
<link rel="stylesheet" href="https://fonts.googleapis.com/css2?family=Didact+Gothic&display=swap">
<style>
  :root {
    --backdrop: #b4b4b4;
    --card: #ffffff;
    --ink: #3a3a3a;
    --ink-soft: #4a4a4a;
    --mauve: #c48c9c;
    --petal-light: #f3e6f2;
    --petal-mid: #c79ac7;
    --petal-deep: #9a5f9e;
    --skin: #e9c9bd;
    --hair: #5b4338;
  }
  * { margin: 0; padding: 0; box-sizing: border-box; }
  html, body {
    width: 1200px; height: 784px; overflow: hidden;
    background: var(--backdrop);
    font-family: "Didact Gothic", "Century Gothic", sans-serif;
  }
  .stage {
    position: relative; width: 1200px; height: 784px;
    display: flex; align-items: center; justify-content: center; gap: 40px;
  }
  .card {
    position: relative; width: 520px; height: 318px;
    background: var(--card); overflow: hidden;
    box-shadow: 0 4px 14px rgba(0,0,0,0.18);
  }
  .brand {
    position: absolute; top: 30px; right: 30px;
    display: flex; align-items: center; gap: 8px;
    color: var(--ink); font-size: 10px; letter-spacing: 1.5px; text-transform: uppercase;
  }
  .brand-dot {
    width: 26px; height: 26px; border-radius: 50%; background: var(--ink);
  }
  .card-back .identity { position: absolute; left: 34px; top: 112px; }
  .person-name {
    font-size: 28px; letter-spacing: 2px; text-transform: uppercase; color: var(--ink);
    font-weight: 400; line-height: 1.1;
  }
  .person-role { font-size: 18px; color: var(--mauve); margin-top: 2px; }
  .contacts {
    position: absolute; left: 34px; top: 194px; list-style: none;
    font-size: 17px; line-height: 25px; color: var(--ink-soft); white-space: nowrap;
  }
  .contacts .label { color: var(--mauve); }
  .contacts .icon-row { display: flex; align-items: center; gap: 8px; }
  .social-mark { width: 14px; height: 14px; background: var(--ink-soft); border-radius: 2px; flex: none; }
  .card-front .visual { position: absolute; inset: 0; }
  .card-front .brand { top: 24px; }
</style>
</head>
<body>
<main class="stage">
  <section class="card card-back" aria-label="Card back">
    <div class="brand"><span class="brand-dot"></span><span>LK Makeup Artistry</span></div>
    <div class="identity">
      <h1 class="person-name">Rosalind Kerr</h1>
      <p class="person-role">Makeup Artist</p>
    </div>
    <ul class="contacts">
      <li><span class="label">Contact number:</span> 0437 295 148</li>
      <li><span class="label">Email:</span> roskerr_makeup@mailvento.com</li>
      <li class="icon-row"><span class="social-mark"></span>www.mybeautypage.net/LKMakeUpArtistry</li>
      <li class="icon-row"><span class="social-mark"></span>@lkmakeupartistry</li>
    </ul>
  </section>

  <section class="card card-front" aria-label="Card front">
    <svg class="visual" width="520" height="318" viewBox="0 0 520 318" role="img"
         aria-label="Portrait of a model with lilac eye makeup beside a large purple and white flower">
      <defs>
        <linearGradient id="portrait-tone" x1="0" y1="0" x2="1" y2="0">
          <stop offset="0" stop-color="var(--hair)"/>
          <stop offset="0.12" stop-color="var(--skin)"/>
          <stop offset="0.3" stop-color="var(--skin)"/>
          <stop offset="0.42" stop-color="var(--petal-light)"/>
          <stop offset="0.7" stop-color="var(--petal-mid)"/>
          <stop offset="1" stop-color="var(--petal-light)"/>
        </linearGradient>
        <radialGradient id="petal-glow" cx="0.65" cy="0.6" r="0.5">
          <stop offset="0" stop-color="var(--petal-deep)" stop-opacity="0.55"/>
          <stop offset="1" stop-color="var(--petal-deep)" stop-opacity="0"/>
        </radialGradient>
      </defs>
      <rect width="520" height="318" fill="url(#portrait-tone)"/>
      <rect width="520" height="318" fill="url(#petal-glow)"/>
    </svg>
    <div class="brand"><span class="brand-dot"></span><span>LK Makeup Artistry</span></div>
  </section>
</main>
</body>
</html>
```